Martin & Ilse Crowther
WE HAVE MOVED
The address of our new home is
Fern Hollow
48 Wexcombe Lane
Thornby on Wyle
Warwickshire
B97 3LT
Tel: 07912 408716
Email: martin@kelvo.uk.com

```html
<!DOCTYPE html>
<html lang="en">
<head>
<meta charset="utf-8">
<title>Martin &amp; Ilse Crowther – We Have Moved</title>
<link rel="stylesheet" href="https://fonts.googleapis.com/css2?family=Montserrat:wght@400;500;600&family=Great+Vibes&display=swap">
<style>
  :root {
    --page-bg: #e9e7e3;
    --card-bg: #ffffff;
    --ink: #232323;
    --gold: #a77b0b;
    --band-text: #fbf6e8;
    --olive-mid: #7d9a45;
    --olive-soft: rgba(125, 154, 69, 0);
  }
  * { margin: 0; padding: 0; box-sizing: border-box; }
  html, body {
    width: 1200px;
    height: 1200px;
    overflow: hidden;
    background: var(--page-bg);
  }
  .moving-card {
    position: absolute;
    left: 210px;
    top: 66px;
    width: 780px;
    height: 1068px;
    background: var(--card-bg);
    overflow: hidden;
    box-shadow: 0 2px 10px rgba(0, 0, 0, 0.08);
    font-family: "Montserrat", Arial, sans-serif;
    color: var(--ink);
  }
  .foliage {
    position: absolute;
    border-radius: 50%;
  }
  .foliage--olive-branch {
    left: 600px; top: 10px; width: 190px; height: 150px;
    background: radial-gradient(ellipse at 60% 45%, var(--olive-mid) 0%, rgba(125,154,69,0.55) 40%, var(--olive-soft) 72%);
  }
  .foliage--left-sprig {
    left: -40px; top: 130px; width: 175px; height: 350px;
    background: radial-gradient(ellipse at 40% 50%, rgba(140,146,115,0.75) 0%, rgba(140,146,115,0.35) 45%, rgba(140,146,115,0) 72%);
  }
  .foliage--right-sprig {
    left: 620px; top: 560px; width: 190px; height: 340px;
    background: radial-gradient(ellipse at 60% 50%, rgba(140,146,115,0.75) 0%, rgba(140,146,115,0.35) 45%, rgba(140,146,115,0) 72%);
  }
  .foliage--bottom-sprig {
    left: -30px; top: 790px; width: 210px; height: 320px;
    background: radial-gradient(ellipse at 40% 55%, rgba(79,106,44,0.7) 0%, rgba(79,106,44,0.3) 45%, rgba(79,106,44,0) 72%);
  }
  .names {
    position: absolute;
    left: 0; right: 0; top: 92px;
    text-align: center;
    font-weight: normal;
  }
  .names__first {
    display: block;
    font-weight: 500;
    font-size: 70px;
    letter-spacing: 4px;
    line-height: 1;
  }
  .names__joiner {
    display: block;
    font-weight: 500;
    font-size: 17px;
    letter-spacing: 2px;
    line-height: 1;
    margin-top: 12px;
  }
  .names__second {
    display: block;
    font-family: "Great Vibes", cursive;
    font-weight: 400;
    font-size: 100px;
    line-height: 1.15;
    margin-top: 14px;
  }
  .announcement {
    position: absolute;
    left: 0; right: 0; top: 378px;
    text-align: center;
    font-size: 20px;
    font-weight: 600;
    letter-spacing: 6px;
    color: var(--gold);
    line-height: 1;
  }
  .address-band {
    position: absolute;
    left: 0; right: 0; top: 450px;
    height: 315px;
    background: var(--gold);
    color: var(--band-text);
    display: flex;
    flex-direction: column;
    align-items: center;
    justify-content: center;
    text-transform: uppercase;
    font-style: normal;
    font-size: 32px;
    line-height: 48px;
    letter-spacing: 1px;
    font-weight: 400;
  }
  .address-band__street { font-weight: 600; }
  .contact {
    position: absolute;
    left: 0; right: 0; top: 885px;
    display: flex;
    flex-direction: column;
    align-items: center;
    gap: 10px;
  }
  .contact__line {
    display: flex;
    align-items: center;
    gap: 16px;
    font-size: 30px;
    font-weight: 500;
    line-height: 1.2;
  }
  .contact__line--email { font-size: 28px; }
  .contact__icon { width: 24px; height: 24px; fill: var(--gold); flex: none; }
</style>
</head>
<body>
  <main class="moving-card">
    <div class="foliage foliage--olive-branch" role="img" aria-label="Olive branch with green olives"></div>
    <div class="foliage foliage--left-sprig" role="img" aria-label="Sprig of olive leaves"></div>
    <div class="foliage foliage--right-sprig" role="img" aria-label="Sprig of olive leaves"></div>
    <div class="foliage foliage--bottom-sprig" role="img" aria-label="Sprig of olive leaves"></div>

    <h1 class="names">
      <span class="names__first">MARTIN</span>
      <span class="names__joiner">AND</span>
      <span class="names__second">Ilse Crowther</span>
    </h1>

    <p class="announcement">WE HAVE MOVED</p>

    <address class="address-band">
      <span class="address-band__house">Fern Hollow</span>
      <span class="address-band__street">48 Wexcombe Lane</span>
      <span class="address-band__town">Thornby on Wyle</span>
      <span class="address-band__county">Warwickshire</span>
      <span class="address-band__postcode">B97 3LT</span>
    </address>

    <div class="contact">
      <p class="contact__line contact__line--phone">
        <svg class="contact__icon" viewBox="0 0 24 24" aria-hidden="true">
          <path d="M6.6 10.8a15.1 15.1 0 0 0 6.6 6.6l2.2-2.2a1 1 0 0 1 1-.25 11.4 11.4 0 0 0 3.6.57 1 1 0 0 1 1 1V20a1 1 0 0 1-1 1A17 17 0 0 1 3 4a1 1 0 0 1 1-1h3.5a1 1 0 0 1 1 1c0 1.25.2 2.45.57 3.57a1 1 0 0 1-.25 1z"/>
        </svg>
        07912 408716
      </p>
      <p class="contact__line contact__line--email">
        <svg class="contact__icon" viewBox="0 0 24 24" aria-hidden="true">
          <path d="M2 5h20v2l-10 6L2 7z"/>
          <path d="M2 9l10 6 10-6v10H2z"/>
        </svg>
        martin@kelvo.uk.com
      </p>
    </div>
  </main>
</body>
</html>
```